LLC needs a business card design that emphasizes consulting and expert witness in upstream oil and g

I need a business card design for my company called Kelvora. My expertise is in oil and gas upstream operations management to optimize performance and also as an expert witness for law firms in oil and gas upstream operations litigation.
The final design should communicate knowledge and hands-on experience as well as trust. (Kelvora means rope or lasso. Perhaps "Kelvora" should be in the form of a rope.) I do not like the color green in any shade. My first preference would be some shade of blue.
Oil And Gas

```html
<!DOCTYPE html>
<html lang="en">
<head>
<meta charset="utf-8">
<title>Kelvora — Business Card</title>
<link rel="stylesheet" href="https://fonts.googleapis.com/css2?family=Lato:wght@400;700&display=swap">
<style>
  :root {
    --stage: #d9d9d6;
    --card: #1c1c1d;
    --accent: #1aa3dc;
    --ink: #ffffff;
    --emboss: #2c2c2d;
  }
  * { box-sizing: border-box; margin: 0; padding: 0; }
  html, body { width: 1200px; height: 800px; overflow: hidden; }
  body {
    background: var(--stage);
    font-family: "Lato", sans-serif;
    display: flex;
    align-items: center;
    justify-content: center;
    gap: 40px;
  }
  .card {
    position: relative;
    width: 540px;
    height: 309px;
    background: var(--card);
    box-shadow: 0 10px 28px rgba(0,0,0,0.25);
  }
  .brand-name {
    position: absolute;
    left: 0; right: 0;
    text-align: center;
    font-weight: 700;
    font-size: 44px;
    line-height: 1;
    letter-spacing: 1px;
  }
  .card-front .brand-name { top: 68px; left: 70px; color: var(--accent); }
  .card-back .brand-name { top: 132px; color: var(--emboss); }
  .person {
    position: absolute;
    right: 290px;
    top: 168px;
    text-align: right;
    color: var(--ink);
    font-size: 14.5px;
    line-height: 1.3;
  }
  .person-name {
    color: var(--accent);
    font-weight: 700;
    font-size: 22px;
    line-height: 1.15;
  }
  .divider {
    position: absolute;
    left: 266px;
    top: 172px;
    width: 1.5px;
    height: 110px;
    background: linear-gradient(to bottom, transparent, var(--accent) 30%, var(--accent) 70%, transparent);
  }
  .contacts {
    position: absolute;
    left: 282px;
    top: 188px;
    list-style: none;
    color: var(--ink);
    font-size: 14.5px;
    line-height: 1.45;
  }
  .contacts li { display: flex; align-items: center; gap: 8px; }
  .contacts svg { width: 12px; height: 12px; fill: var(--accent); flex: none; }
</style>
</head>
<body>
  <section class="card card-front" aria-label="Card front">
    <div class="brand-name">Kelvora</div>
    <div class="person">
      <div class="person-name">Daniel Harlow</div>
      <div class="person-title">Managing Director</div>
      <div>4410, Ridge Avenue</div>
      <div>Eastfield, Portvale 51730</div>
    </div>
    <div class="divider"></div>
    <ul class="contacts">
      <li><svg viewBox="0 0 12 12" aria-hidden="true"><path d="M2.5 0.8l2 2.2-1 1.3c.6 1.5 1.7 2.6 3.2 3.2l1.3-1 2.2 2-1.1 1.9C5 10.3 1.7 7 0.6 1.9z"/></svg>+(555) 014 2290</li>
      <li><svg viewBox="0 0 12 12" aria-hidden="true"><path d="M3 0h6v12H3zM4 1.5v7.5h4V1.5zM5.5 10h1v1h-1z" fill-rule="evenodd"/></svg>+(555) 017 3861</li>
      <li><svg viewBox="0 0 12 12" aria-hidden="true"><path d="M0 2h12v1L6 7 0 3zM0 4.2l6 4 6-4V10H0z"/></svg>dharlow@kelvora.com</li>
      <li><svg viewBox="0 0 12 12" aria-hidden="true"><path d="M7 0.5a4.5 4.5 0 1 1 0 9 4.5 4.5 0 0 1 0-9zm0 1.5a3 3 0 1 0 0 6 3 3 0 0 0 0-6zM3.6 7.3l1.1 1.1L1.2 11.9 0.1 10.8z"/></svg>www.kelvora.com</li>
    </ul>
  </section>

  <section class="card card-back" aria-label="Card back">
    <div class="brand-name">Kelvora</div>
  </section>
</body>
</html>
```